Business cards, Stationary, E-mail signature, leterhead, fax coversheet, thank you card, invoice tem
Torvan Networks Stationary - please read brief
Business cards, Stationary, E-mail signature, leterhead, fax coversheet, thank you card, invoice tem -
Creative Brief
Use specific fonts
Use the best that will go with the logo design
Professional
Brent Oakley
71523 Birch Ridge Court, Suite 204 Sterling, VA 20783
BrentO@torvannetworks.example
www.torvannetworks.example
Use the icon on the left side of the logo only

```html
<!DOCTYPE html>
<html lang="en">
<head>
<meta charset="utf-8">
<title>Torvan Networks Business Cards</title>
<link href="https://fonts.googleapis.com/css2?family=Arimo:wght@400;700&display=swap" rel="stylesheet">
<style>
:root{
  --bg:#e9e7e4;
  --card:#ffffff;
  --navy:#1d3a7a;
  --blue:#2f63b4;
  --sky:#5d92d6;
  --silver:#b9bdc4;
  --tag:#5a6478;
  --white:#ffffff;
}
*{margin:0;padding:0;box-sizing:border-box}
html,body{width:1200px;height:852px;overflow:hidden;background:var(--bg);font-family:"Arimo",Arial,sans-serif}
.stage{position:relative;width:1200px;height:852px}
.card{position:absolute;width:540px;height:310px;border-radius:16px;background:var(--card);overflow:hidden;box-shadow:0 6px 18px rgba(0,0,0,.18)}
.card-front{left:70px;top:80px}
.card-alt{left:590px;top:460px}
.card svg.wave{position:absolute;inset:0;width:100%;height:100%}
.brand{position:absolute;left:28px;display:flex;align-items:center;gap:10px}
.brand-mark{width:40px;height:40px;border-radius:8px;background:var(--navy);flex:none}
.brand-name{font-weight:700;font-size:22px;color:var(--navy);letter-spacing:.5px;line-height:1;white-space:nowrap}
.brand-tag{font-size:7.5px;color:var(--tag);letter-spacing:.5px;margin-top:5px;text-transform:uppercase;white-space:nowrap}
.card-front .brand{top:42px}
.card-alt .brand{top:72px}
.holder{position:absolute;font-weight:700;font-size:20px;white-space:nowrap}
.card-front .holder{right:28px;top:18px;color:var(--navy)}
.card-alt .holder{left:30px;bottom:24px;color:var(--white)}
.details{position:absolute;right:26px;text-align:right;font-size:11px;line-height:17px;white-space:nowrap}
.card-front .details{top:125px;color:var(--white)}
.card-alt .details{top:36px;color:var(--navy)}
.details .row{display:flex;justify-content:flex-end;align-items:center;gap:6px}
.details .gap{height:8px}
.icon{width:11px;height:11px;flex:none}
</style>
</head>
<body>
<main class="stage">

  <section class="card card-front">
    <svg class="wave" viewBox="0 0 540 310" aria-hidden="true">
      <defs>
        <linearGradient id="frontBlue" x1="0" y1="1" x2="1" y2="0">
          <stop offset="0" stop-color="#1d3a7a"/>
          <stop offset=".6" stop-color="#2f63b4"/>
          <stop offset="1" stop-color="#5d92d6"/>
        </linearGradient>
      </defs>
      <path d="M120 310 C262 300 190 80 540 58 L540 310 Z" fill="#b9bdc4"/>
      <path d="M150 310 C290 300 220 100 540 80 L540 310 Z" fill="url(#frontBlue)"/>
    </svg>
    <div class="brand">
      <span class="brand-mark"></span>
      <div>
        <div class="brand-name">TORVAN NETWORKS</div>
        <div class="brand-tag">IT · Management Consulting · Staffing</div>
      </div>
    </div>
    <div class="holder">Brent Oakley</div>
    <div class="details">
      <div>71523 Birch Ridge Court,</div>
      <div>Suite 204, Sterling, VA 20783</div>
      <div class="gap"></div>
      <div class="row">555 010 4821
        <svg class="icon" viewBox="0 0 12 12"><path d="M2 1h3l1 3-2 1a7 7 0 0 0 3 3l1-2 3 1v3c-6 0-9-3-9-9z" fill="currentColor"/></svg></div>
      <div class="row">555 010 4822
        <svg class="icon" viewBox="0 0 12 12"><rect x="2" y="1" width="8" height="4" fill="currentColor"/><rect x="1" y="6" width="10" height="5" rx="1" fill="currentColor"/></svg></div>
      <div class="row">BrentO@torvannetworks.example
        <svg class="icon" viewBox="0 0 12 12"><circle cx="6" cy="6" r="5" fill="none" stroke="currentColor" stroke-width="1.4"/><circle cx="6" cy="6" r="2" fill="currentColor"/></svg></div>
      <div class="row">www.torvannetworks.example
        <svg class="icon" viewBox="0 0 12 12"><circle cx="6" cy="6" r="5" fill="none" stroke="currentColor" stroke-width="1.2"/><path d="M1 6h10M6 1c-3 3-3 7 0 10M6 1c3 3 3 7 0 10" fill="none" stroke="currentColor" stroke-width="1"/></svg></div>
    </div>
  </section>

  <section class="card card-alt">
    <svg class="wave" viewBox="0 0 540 310" aria-hidden="true">
      <defs>
        <linearGradient id="altBlue" x1="0" y1="1" x2="1" y2="0">
          <stop offset="0" stop-color="#1d3a7a"/>
          <stop offset=".55" stop-color="#2f63b4"/>
          <stop offset="1" stop-color="#5d92d6"/>
        </linearGradient>
      </defs>
      <path d="M0 310 L0 232 C170 268 380 240 540 150 L540 310 Z" fill="#b9bdc4"/>
      <path d="M0 310 L0 254 C170 290 390 262 540 172 L540 310 Z" fill="url(#altBlue)"/>
    </svg>
    <div class="brand">
      <span class="brand-mark"></span>
      <div>
        <div class="brand-name">TORVAN NETWORKS</div>
        <div class="brand-tag">IT · Management Consulting · Staffing</div>
      </div>
    </div>
    <div class="details">
      <div>71523 Birch Ridge Court,</div>
      <div>Suite 204, Sterling, VA 20783</div>
      <div class="gap"></div>
      <div class="row">555 010 4821
        <svg class="icon" viewBox="0 0 12 12"><path d="M2 1h3l1 3-2 1a7 7 0 0 0 3 3l1-2 3 1v3c-6 0-9-3-9-9z" fill="currentColor"/></svg></div>
      <div class="row">555 010 4822
        <svg class="icon" viewBox="0 0 12 12"><rect x="2" y="1" width="8" height="4" fill="currentColor"/><rect x="1" y="6" width="10" height="5" rx="1" fill="currentColor"/></svg></div>
      <div class="row">BrentO@torvannetworks.example
        <svg class="icon" viewBox="0 0 12 12"><circle cx="6" cy="6" r="5" fill="none" stroke="currentColor" stroke-width="1.4"/><circle cx="6" cy="6" r="2" fill="currentColor"/></svg></div>
      <div class="row">www.torvannetworks.example
        <svg class="icon" viewBox="0 0 12 12"><circle cx="6" cy="6" r="5" fill="none" stroke="currentColor" stroke-width="1.2"/><path d="M1 6h10M6 1c-3 3-3 7 0 10M6 1c3 3 3 7 0 10" fill="none" stroke="currentColor" stroke-width="1"/></svg></div>
    </div>
    <div class="holder">Brent Oakley</div>
  </section>

</main>
</body>
</html>
```